Up and coming Australian Systems Integrator needs a proposal template refresh

We need to update our proposal template and are looking for a fresh, modern, simple and elegant proposal template. We'd like to keep our existing logos if possible.
Quorvex is a privately owned company operating since 2006. Offices and technical staff located in Port Melbourne and Bendigo
Sustained, profitable growth year on year
Velmar strategic partner
Velmar Advanced Enterprise Network Architecture Specialisation
Velmar Advanced Security Architecture Specialisation
Velmar Advanced Collaboration Architecture Specialisation
Velmar Advanced Unified Computing Technology Specialisation
Velmar Advanced Data Centre Architecture Specialisation (in progress)
Velmar Gold Partner – Expect 2H2018
As well as being a Velmar partner we have a well established stable of other vendors such as Brandova, Teskaro, Haldenworth, ZEP, Mirvale Interactive, Dulm, TidePoint, KoMELDA Gate)
We are a top two provider of Velmar product/services in the Victorian healthcare sector.
Please feel free to use different colors and fonts as we feel the existing ones look dated.

```html
<!DOCTYPE html>
<html lang="en">
<head>
<meta charset="utf-8">
<title>Quorvex Proposal Template</title>
<link href="https://fonts.googleapis.com/css2?family=Michroma&family=Orbitron:wght@700;800&family=Montserrat:wght@400;500;600;700&display=swap" rel="stylesheet">
<style>
:root{
  --backdrop:#efcbb3;
  --paper:#ffffff;
  --navy:#16379a;
  --navy-dark:#0f2a78;
  --ink:#4a4a4a;
  --grey-band:#6e6e70;
  --table-head:#6b6b6d;
  --row-tint:#ebebec;
  --rule:#c9c9cb;
  --icon:#1c5aa6;
  --silver:#8a8d92;
}
*{box-sizing:border-box;margin:0;padding:0}
html,body{width:920px;height:1200px;overflow:hidden;background:var(--backdrop)}
body{font-family:"Montserrat",Arial,sans-serif;color:var(--ink);position:relative}
.page{position:absolute;top:296px;width:430px;height:608px;background:var(--paper);overflow:hidden;box-shadow:0 2px 8px rgba(0,0,0,.12)}
.page--cover{left:20px}
.page--inner{left:470px}

.brand{display:flex;flex-direction:column;align-items:flex-start}
.brand__row{display:flex;align-items:center;gap:8px}
.brand__mark{width:12px;height:12px;background:var(--navy)}
.brand__name{font-family:"Michroma",sans-serif;color:var(--navy);letter-spacing:1px;line-height:1}
.brand__tag{font-family:"Montserrat",sans-serif;color:var(--silver);letter-spacing:1.2px;text-transform:uppercase;line-height:1}

.cover__brand{position:absolute;top:44px;left:0;right:0;align-items:center}
.cover__brand .brand__name{font-size:25px}
.cover__brand .brand__tag{font-size:7px;margin-top:4px;margin-left:20px}

.cover__title{position:absolute;top:112px;left:10px;right:10px;text-align:center;font-family:"Orbitron",sans-serif;font-weight:800;font-size:13.5px;line-height:20px;color:var(--navy);letter-spacing:.4px;white-space:nowrap}
.cover__intro{position:absolute;top:162px;left:24px;right:24px;text-align:center;font-size:8.6px;line-height:12px;color:#555}

.services{position:absolute;top:228px;left:18px;right:18px;display:flex;justify-content:space-between;list-style:none}
.service{width:62px;display:flex;flex-direction:column;align-items:center;text-align:center;font-size:7px;line-height:8px;color:#444}
.service svg{width:22px;height:22px;margin-bottom:6px}

.cover__photo{position:absolute;top:308px;left:0;width:430px;height:248px;background:radial-gradient(ellipse at 62% 55%,#3f6fb8 0%,#1e3f86 45%,#0e2356 100%)}

.footer{position:absolute;left:0;right:0;bottom:0;height:38px;background:var(--grey-band);display:flex;align-items:center;justify-content:center;color:#fff;font-size:10px;white-space:nowrap}
.footer__item{display:flex;align-items:center;gap:6px;padding:0 10px}
.footer__item + .footer__item{border-left:1px solid rgba(255,255,255,.7)}
.footer__item svg{width:9px;height:9px}

.inner__bar{position:absolute;top:32px;left:0;width:276px;height:13px}
.inner__brand{position:absolute;top:30px;left:282px}
.inner__brand .brand__name{font-size:13px}
.inner__brand .brand__row{gap:5px}
.inner__brand .brand__mark{width:8px;height:8px}
.inner__brand .brand__tag{font-size:3.6px;margin-top:2px;margin-left:13px}

.section{position:absolute;left:17px;right:17px}
.section__title{text-align:center;font-size:12.5px;font-weight:700;color:var(--navy-dark);letter-spacing:.2px;margin-bottom:7px}
.grid{width:100%;border-collapse:collapse;table-layout:fixed}
.grid th{background:var(--table-head);color:#fff;font-weight:400;font-size:9px;height:19px;text-transform:uppercase;letter-spacing:.2px}
.grid td{height:19px}
.grid tr:nth-child(odd) td{background:var(--row-tint)}
.grid th + th,.grid td + td{border-left:2px solid var(--rule)}
.section--control{top:66px}
.section--distribution{top:232px}
.section--definitions{top:398px}
.grid--terms col.term{width:131px}
</style>
</head>
<body>

<section class="page page--cover">
  <header class="brand cover__brand">
    <div class="brand__row"><span class="brand__mark"></span><span class="brand__name">QUORVEX</span></div>
    <span class="brand__tag">Network &amp; Communications Solutions</span>
  </header>

  <h1 class="cover__title">LOREM IPSUM DOLOR SIT AMET, CONSE<br>CTETUR ADIPISCING ELIT</h1>
  <p class="cover__intro">Sed do eiusmod tempor incididunt ut labore et dolore magna aliqua. Ut enim ad minim veniam, abore et dolore magna aliqua. Ut enim ad minim veniam.</p>

  <ul class="services">
    <li class="service">
      <svg viewBox="0 0 24 24"><rect x="2" y="3" width="6" height="18" fill="var(--icon)"/><rect x="9" y="3" width="13" height="18" fill="none" stroke="var(--icon)" stroke-width="2"/><g fill="var(--icon)"><rect x="11" y="6" width="9" height="3"/><rect x="11" y="11" width="2" height="2"/><rect x="14.5" y="11" width="2" height="2"/><rect x="18" y="11" width="2" height="2"/><rect x="11" y="15" width="2" height="2"/><rect x="14.5" y="15" width="2" height="2"/><rect x="18" y="15" width="2" height="2"/></g></svg>
      Unified Communications
    </li>
    <li class="service">
      <svg viewBox="0 0 24 24"><circle cx="12" cy="12" r="11" fill="var(--icon)"/><path d="M8.5 11V8.5a3.5 3.5 0 0 1 7 0V11" fill="none" stroke="#fff" stroke-width="1.8"/><rect x="7" y="11" width="10" height="7" rx="1" fill="#fff"/><circle cx="12" cy="14.5" r="1.3" fill="var(--icon)"/></svg>
      Security
    </li>
    <li class="service">
      <svg viewBox="0 0 24 24"><circle cx="12" cy="12" r="10.5" fill="none" stroke="var(--icon)" stroke-width="2"/><path d="M12 4v16M4 12h16" stroke="var(--icon)" stroke-width="2"/><path d="M12 4l-2.5 3h5zM12 20l-2.5-3h5zM4 12l3-2.5v5zM20 12l-3-2.5v5z" fill="var(--icon)"/></svg>
      Foundation Networking
    </li>
    <li class="service">
      <svg viewBox="0 0 24 24"><path d="M6 17a4 4 0 0 1 0-8 6 6 0 0 1 11.5-1.5A4.5 4.5 0 0 1 18 17z" fill="var(--icon)"/><path d="M12 12v10M9 19h6" stroke="var(--icon)" stroke-width="2"/><path d="M12 9l-3 3h6z" fill="#fff"/></svg>
      Data Centre
    </li>
    <li class="service">
      <svg viewBox="0 0 24 24"><rect x="1" y="1" width="22" height="22" fill="#1b5d93"/><path d="M3 14h6l2-5 2 8 2-4h6" fill="none" stroke="#7fd3ff" stroke-width="1.2"/></svg>
      Alerting &amp; Messaging
    </li>
    <li class="service">
      <svg viewBox="0 0 24 24"><circle cx="5" cy="19" r="2.5" fill="var(--icon)"/><path d="M3 11a10 10 0 0 1 10 10M3 5a16 16 0 0 1 16 16" fill="none" stroke="var(--icon)" stroke-width="2.6"/></svg>
      Wireless Networking
    </li>
  </ul>

  <div class="cover__photo" role="img" aria-label="Photo of a hand holding a tablet with a glowing city skyline and network icons above it, against a night sky"></div>

  <footer class="footer">
    <span class="footer__item"><svg viewBox="0 0 10 10"><circle cx="5" cy="5" r="4.3" fill="none" stroke="#fff" stroke-width="1"/><path d="M1 5h8M5 .7v8.6" stroke="#fff" stroke-width=".8"/></svg>www.quorvex.net.au</span>
    <span class="footer__item"><svg viewBox="0 0 10 10"><rect x=".5" y="2" width="9" height="6.5" fill="#fff"/><path d="M.5 2L5 5.5 9.5 2" fill="none" stroke="var(--grey-band)" stroke-width=".8"/></svg>info@quorvex.net.au</span>
    <span class="footer__item"><svg viewBox="0 0 10 10"><path d="M1 4c0-2 1-3 4-3s4 1 4 3H7V3H3v1zM2.5 5h5l1 4h-7z" fill="#fff"/></svg>1800 555 013</span>
  </footer>
</section>

<section class="page page--inner">
  <svg class="inner__bar" viewBox="0 0 276 13" preserveAspectRatio="none"><polygon points="0,0 276,0 266,13 0,13" fill="var(--navy)"/></svg>
  <header class="brand inner__brand">
    <div class="brand__row"><span class="brand__mark"></span><span class="brand__name">QUORVEX</span></div>
    <span class="brand__tag">Network &amp; Communications Solutions</span>
  </header>

  <div class="section section--control">
    <h2 class="section__title">DOCUMENT CONTROL</h2>
    <table class="grid">
      <thead><tr><th>Version Author</th><th>Description</th><th>Approval</th></tr></thead>
      <tbody><tr><td></td><td></td><td></td></tr><tr><td></td><td></td><td></td></tr><tr><td></td><td></td><td></td></tr><tr><td></td><td></td><td></td></tr><tr><td></td><td></td><td></td></tr></tbody>
    </table>
  </div>

  <div class="section section--distribution">
    <h2 class="section__title">DISTRIBUTION LIST</h2>
    <table class="grid">
      <thead><tr><th>Name</th><th>Company</th><th>Role</th></tr></thead>
      <tbody><tr><td></td><td></td><td></td></tr><tr><td></td><td></td><td></td></tr><tr><td></td><td></td><td></td></tr><tr><td></td><td></td><td></td></tr><tr><td></td><td></td><td></td></tr></tbody>
    </table>
  </div>

  <div class="section section--definitions">
    <h2 class="section__title">DEFINITIONS</h2>
    <table class="grid grid--terms">
      <colgroup><col class="term"><col></colgroup>
      <thead><tr><th>Term</th><th>Definition</th></tr></thead>
      <tbody><tr><td></td><td></td></tr><tr><td></td><td></td></tr><tr><td></td><td></td></tr><tr><td></td><td></td></tr><tr><td></td><td></td></tr></tbody>
    </table>
  </div>

  <footer class="footer">
    <span class="footer__item"><svg viewBox="0 0 10 10"><circle cx="5" cy="5" r="4.3" fill="none" stroke="#fff" stroke-width="1"/><path d="M1 5h8M5 .7v8.6" stroke="#fff" stroke-width=".8"/></svg>www.quorvex.net.au</span>
    <span class="footer__item"><svg viewBox="0 0 10 10"><rect x=".5" y="2" width="9" height="6.5" fill="#fff"/><path d="M.5 2L5 5.5 9.5 2" fill="none" stroke="var(--grey-band)" stroke-width=".8"/></svg>info@quorvex.net.au</span>
    <span class="footer__item"><svg viewBox="0 0 10 10"><path d="M1 4c0-2 1-3 4-3s4 1 4 3H7V3H3v1zM2.5 5h5l1 4h-7z" fill="#fff"/></svg>1800 555 013</span>
  </footer>
</section>

</body>
</html>
```